New Quill Harbor Systems website Home Page (design only)

We are looking for a new design for our home page. Please access this url to see a mock-up for you to use
https://pelorabeats.example-sites.com/qhswebsite01. We would like the website to be "alive" so we are open to creative ideas for animated gifs and motion graphics but want to make sure that the overall feel and use of the movement communicates a high tech and innovative company. Please follow the Quillharbor brand guidelines attached. A good example of a website that we feel really meets the innovative feel with movement is https://k7.example/. Do not copy this website! We are providing it as a example for you.

```html
<!DOCTYPE html>
<html lang="en">
<head>
<meta charset="utf-8">
<title>Quillharbor – Home</title>
<link rel="stylesheet" href="https://fonts.googleapis.com/css2?family=Jost:wght@400;500;600&family=Nunito+Sans:wght@400;600;700&display=swap">
<style>
:root{
  --navy:#06132b;
  --navy-2:#081a38;
  --navy-3:#0a1f42;
  --teal:#1fa58f;
  --teal-2:#2bc0a2;
  --blue:#1b4fa8;
  --text:#ffffff;
  --muted:#a9b6cc;
}
*{box-sizing:border-box;margin:0;padding:0}
html,body{width:1200px;height:4938px;overflow:hidden}
body{position:relative;background:var(--navy);color:var(--text);font-family:"Nunito Sans",sans-serif}
.abs{position:absolute}
.heading{font-family:"Jost",sans-serif;font-weight:500;text-transform:uppercase;text-align:center;font-size:35px;letter-spacing:.5px;left:0;width:1200px}
.rule{position:absolute;left:573px;width:54px;height:3px;background:var(--teal)}
.lead{position:absolute;left:150px;width:900px;text-align:center;font-size:15px;line-height:28px;color:var(--muted)}
.brand{font-family:"Jost",sans-serif;font-weight:500;font-size:30px;color:#fff;line-height:40px}
.btn{position:absolute;display:flex;align-items:center;justify-content:center;border-radius:26px;font-family:"Jost",sans-serif;font-weight:500;font-size:14px;text-transform:uppercase;color:#fff;border:2px solid var(--teal)}

.site-nav{display:flex;gap:26px;font-size:12px;font-weight:600;text-transform:uppercase}
.site-nav .active{color:var(--teal-2)}
.contact-row{display:flex;gap:18px;font-size:13px;color:#dfe6f2;align-items:center}
.contact-row .ic{color:var(--teal-2);margin-right:6px}

.hero-title{font-family:"Jost",sans-serif;font-weight:500;font-size:36px;line-height:50px;text-align:center;text-transform:uppercase;left:0;width:1200px;top:308px}
.hero-sub{left:270px;width:660px;text-align:center;font-size:16px;line-height:29px;top:422px}

.sol-card{position:absolute;top:1045px;width:231px;height:306px;border:2px solid #b9c4d6;border-radius:8px;text-align:center;padding:28px 12px 0}
.sol-card.featured{background:linear-gradient(160deg,var(--teal),var(--blue));border-color:#7fb9e8}
.sol-icon{width:72px;height:72px;border-radius:50%;margin:0 auto 18px;background:linear-gradient(135deg,var(--teal-2),#1a5aa8);display:flex;align-items:center;justify-content:center}
.sol-icon span{width:28px;height:24px;border:2px solid #fff;border-radius:3px}
.sol-card.featured .sol-icon{background:#fff}
.sol-card.featured .sol-icon span{border-color:var(--blue)}
.sol-card h3{font-family:"Jost",sans-serif;font-weight:500;font-size:17px;margin-bottom:10px}
.sol-card p{font-size:11.5px;line-height:21px;color:#e6ecf5}

.market-bg{left:0;top:1457px;width:1200px;height:872px;background:var(--navy-3)}
.tile{position:absolute;width:313px;height:221px;border:2px solid #9fb0c8;border-radius:6px;display:flex;align-items:center;justify-content:center;text-align:center;font-family:"Jost",sans-serif;font-weight:500;font-size:16px;text-transform:uppercase;padding:0 20px}
.tile.featured{background:linear-gradient(160deg,var(--teal),#1d5fae);align-items:flex-end;padding-bottom:60px}

.tabs{left:111px;top:2525px;width:976px;display:flex;gap:22px}
.tab{flex:1;border-top:2px solid #b6c1d3;padding-top:14px;font-size:15px;font-weight:600}
.tab.active{border-color:var(--teal);color:var(--teal)}
.feature-title{font-family:"Jost",sans-serif;font-weight:500;font-size:33px;color:var(--teal-2);text-transform:uppercase}
.feature-list{list-style:none;width:447px}
.feature-list li{position:relative;padding-left:30px;font-size:13px;line-height:23px;color:#c8d2e2;margin-bottom:9px;text-align:justify}
.feature-list li::before{content:"";position:absolute;left:0;top:6px;width:11px;height:11px;border-radius:50%;border:2px solid var(--blue);background:var(--teal)}

.cta-band{left:0;top:3098px;width:1200px;height:262px;background:linear-gradient(100deg,#148a7d 0%,#0f5a8a 55%,#1a3fa0 100%)}
.btn.light{background:#fff;color:var(--navy);border-color:#fff}
.btn.outline{border-color:#fff}

.news-card{position:absolute;background:#0a1a36;box-shadow:0 6px 24px rgba(0,0,0,.35)}
.news-meta{display:flex;align-items:center;gap:10px;font-size:11px;color:#9fb0c8}
.news-meta i{width:22px;height:22px;border-radius:50%;background:var(--blue);display:inline-block}
.news-title{font-family:"Jost",sans-serif;font-weight:500;font-size:16px;line-height:24px;text-transform:uppercase}
.news-excerpt{font-size:13px;line-height:23px;color:#9fb0c8}
.read-more{font-size:11px;font-weight:700;color:var(--teal-2);text-transform:uppercase}

.customer{position:absolute;top:4428px;width:177px;height:83px;background:#0d2146;display:flex;align-items:center;justify-content:center;font-family:"Jost",sans-serif;font-weight:500;font-size:20px;color:#fff}
.arrow{position:absolute;top:4455px}

.footer-nav{display:flex;gap:26px;font-size:12px;font-weight:600;text-transform:uppercase;justify-content:center;width:1200px;left:0}
.social{display:flex;gap:8px;left:530px}
.social i{width:28px;height:28px;border-radius:50%;background:#3c66b6;display:block}
</style>
</head>
<body>

<svg class="abs" style="left:0;top:0" width="1200" height="800" viewBox="0 0 1200 800" role="img" aria-label="Glowing digital network of data points and padlock icons over a dark blue field">
  <defs>
    <radialGradient id="heroGlow" cx="50%" cy="55%" r="60%">
      <stop offset="0" stop-color="#2a5a9a"/>
      <stop offset=".5" stop-color="#0f2b55"/>
      <stop offset="1" stop-color="#06132b"/>
    </radialGradient>
    <linearGradient id="arc" x1="0" x2="1">
      <stop offset="0" stop-color="#1fa58f"/>
      <stop offset="1" stop-color="#1b4fa8"/>
    </linearGradient>
  </defs>
  <path d="M0 0H1200V610Q600 1010 0 610Z" fill="url(#heroGlow)"/>
  <path d="M0 610Q600 1010 1200 610" fill="none" stroke="url(#arc)" stroke-width="6"/>
</svg>

<div class="abs brand" style="left:111px;top:40px">Quillharbor</div>
<div class="abs contact-row" style="left:615px;top:32px">
  <span><span class="ic">&#9742;</span>123-456-7890</span><span style="color:#6d7c95">|</span>
  <span><span class="ic">&#9993;</span>info@quillharbor.example</span>
</div>
<div class="btn" style="left:943px;top:20px;width:145px;height:46px;background:var(--navy);font-size:13px">Book Demo</div>
<nav class="abs site-nav" style="left:419px;top:92px">
  <span class="active">Home</span><span>Solutions</span><span>How it works</span><span>Our market</span><span>Data value</span><span>IDE</span><span>About</span><span>Contact</span>
</nav>

<h1 class="abs hero-title">Your data<br>connection to web 3.0</h1>
<p class="abs hero-sub">Quillharbor’s patented SaaS platform transforms your data into crypto tokens to trade on our Insight Trading Floor®</p>
<div class="btn" style="left:526px;top:510px;width:146px;height:46px;background:var(--teal);font-size:13px">Learn more</div>

<h2 class="abs heading" style="top:862px">Our solutions</h2>
<div class="rule" style="top:915px"></div>
<p class="lead" style="top:944px">Quill Harbor Systems provides a number of solutions for your business, from a marketplace to trade data to a cutting edge method of increasing customer engagements.</p>

<div class="sol-card" style="left:111px"><div class="sol-icon"><span></span></div><h3>TradeLedger®</h3><p>Our Insight Trading Floor® is a multifunctional, patented, data exchange platform empowering users with the knowledge they need to trade any kind of data within a safe environment.</p></div>
<div class="sol-card" style="left:360px"><div class="sol-icon"><span></span></div><h3>Quillharbor® NFT</h3><p>Quillharbor® NFT standardizes pricing by making every token and data type interchangeable with any other, regardless of its source. We randomly generate a token value in a secure format making your data</p></div>
<div class="sol-card featured" style="left:608px"><div class="sol-icon"><span></span></div><h3>GiveStream®</h3><p>The GiveStream® platform provides non-profit organizations and businesses the ability to donate unused data to others in need of key insights to better inform business decisions, fundraising endeavors,</p></div>
<div class="sol-card" style="left:857px"><div class="sol-icon"><span></span></div><h3>Vexa® Platform</h3><p>The Vexa® platform delivers individualized content that immediately increases engagement over any communication medium using patented Vexa® data packets.</p></div>

<div class="abs market-bg"></div>
<h2 class="abs heading" style="top:1519px">Our market</h2>
<div class="rule" style="top:1572px"></div>
<p class="lead" style="top:1598px">Your data is a form of capital that can be monetized as a new revenue stream, mined for business insights, or used to generate new products and services.</p>

<div class="tile" role="img" aria-label="Scientist working at a laboratory bench" style="left:111px;top:1693px;background:linear-gradient(135deg,#3a5b8a,#1a2b4a)">Biotech</div>
<div class="tile featured" style="left:443px;top:1693px">Financial institution</div>
<div class="tile" role="img" aria-label="Gaming room lit in red and blue neon" style="left:774px;top:1693px;background:linear-gradient(135deg,#b0305a,#2a1f6a)">Gaming &amp; Esports</div>
<div class="tile" role="img" aria-label="Medical worker at a hospital computer" style="left:111px;top:1936px;background:linear-gradient(135deg,#c7d6e4,#5d7d9e)">Hospitals &amp; Medical</div>
<div class="tile" role="img" aria-label="Hand holding a glowing tablet in a suit" style="left:443px;top:1936px;background:linear-gradient(160deg,#1a2c4a,#0a1428)">Insuarances</div>
<div class="tile" role="img" aria-label="Hands on a laptop with shopping icons" style="left:774px;top:1936px;background:linear-gradient(135deg,#8a8f96,#3b3f47)">Retail &amp;<br>consumer goods</div>

<div class="btn" style="left:510px;top:2205px;width:180px;height:48px;background:var(--navy-3);font-size:13px">View all market</div>

<h2 class="abs heading" style="top:2414px">Quillharbor plateforms</h2>
<div class="rule" style="top:2467px"></div>
<div class="abs tabs">
  <div class="tab active">Foundry</div><div class="tab">Quillharbor</div><div class="tab">Insight Trading Floor</div><div class="tab">NFT Exchange</div>
</div>
<div class="abs" role="img" aria-label="Hands typing on a laptop with floating profile cards" style="left:111px;top:2628px;width:472px;height:359px;border:2px solid #9fb0c8;border-radius:4px;background:linear-gradient(135deg,#2a5c9a,#0d2448)"></div>
<div class="abs" style="left:640px;top:2640px">
  <div class="feature-title">Foundry</div>
  <div style="font-size:15px;font-weight:700;margin:10px 0 22px;text-transform:uppercase">Make your data work for you.</div>
  <ul class="feature-list">
    <li>Capture structured and unstructured data from different locations (audio, video, image, script).</li>
    <li>Transform data into standardized, saleable “objects” using machine learning and artificial intelligence.</li>
    <li>Retain 100% control over your data assets.</li>
    <li>Extract value of business intelligence.</li>
    <li>Use AI-driven insights to uncover hidden value and develop new visualizations.</li>
  </ul>
</div>

<div class="abs cta-band"></div>
<h2 class="abs heading" style="top:3154px">Take the next step</h2>
<div class="btn outline" style="left:238px;top:3246px;width:230px;height:48px">Contact sales</div>
<div class="btn light" style="left:483px;top:3246px;width:232px;height:48px">Schedule a demo</div>
<div class="btn outline" style="left:730px;top:3246px;width:230px;height:48px">Request information</div>

<h2 class="abs heading" style="top:3450px">Quillharbor in the news</h2>
<div class="rule" style="top:3503px"></div>
<p class="lead" style="top:3529px">Whether you’re a business in need of market data, a developer in the blockchain space, or simply an individual who trades in NFTs - Quillharbor has a solution</p>

<article class="news-card" style="left:119px;top:3629px;width:464px;height:444px">
  <div role="img" aria-label="Hand reaching toward a glowing digital globe" style="height:284px;background:linear-gradient(135deg,#1d3f78,#0a1630)"></div>
  <div style="padding:18px 22px">
    <div class="news-meta"><i></i>12 OCT 2022</div>
    <div class="news-title" style="margin:14px 0 14px">Emerging artists to be launched under brand name ‘Tidemark’</div>
    <div class="read-more">Read more &#10148;</div>
  </div>
</article>
<article class="news-card" style="left:615px;top:3629px;width:472px;height:201px;display:flex">
  <div role="img" aria-label="Person working at a glowing multi-screen desk" style="width:200px;height:201px;background:linear-gradient(135deg,#3a6aa0,#0c1c3a)"></div>
  <div style="padding:20px 24px;flex:1">
    <div class="news-meta"><i></i>12 OCT 2022</div>
    <div class="news-title" style="margin:10px 0 8px">I'm an image title</div>
    <div class="news-excerpt">Sed ut perspiciatis unde omnis iste error sit voluptatemea...</div>
    <div class="read-more" style="margin-top:10px">Read more &#10148;</div>
  </div>
</article>
<article class="news-card" style="left:615px;top:3866px;width:472px;height:196px;display:flex">
  <div role="img" aria-label="Hand holding a glowing network of figures" style="width:200px;height:196px;background:linear-gradient(135deg,#2d4f80,#0c1a34)"></div>
  <div style="padding:20px 24px;flex:1">
    <div class="news-meta"><i></i>12 OCT 2022</div>
    <div class="news-title" style="margin:10px 0 8px">I'm an image title</div>
    <div class="news-excerpt">Sed ut perspiciatis unde omnis iste error sit voluptatemea...</div>
    <div class="read-more" style="margin-top:10px">Read more &#10148;</div>
  </div>
</article>

<h2 class="abs heading" style="top:4251px">Quillharbor customers</h2>
<div class="rule" style="top:4304px"></div>
<p class="lead" style="top:4332px">By leveraging data, optimizing performance and constantly improving our data-delivery solutions, we help our clients align their digital transformations with their core business and trading strategies.</p>
<svg class="arrow" style="left:44px" width="26" height="30" viewBox="0 0 26 30"><path d="M18 3L6 15l12 12" fill="none" stroke="#2bc0a2" stroke-width="5"/></svg>
<div class="customer" style="left:111px">Vexa</div>
<div class="customer" style="left:311px">Northwind</div>
<div class="customer" style="left:512px">Cirrolane</div>
<div class="customer" style="left:711px">Halden Wire</div>
<div class="customer" style="left:911px">Paylume</div>
<svg class="arrow" style="left:1128px" width="26" height="30" viewBox="0 0 26 30"><path d="M8 3l12 12L8 27" fill="none" stroke="#fff" stroke-width="5"/></svg>

<svg class="abs" style="left:0;top:4575px" width="1200" height="363" viewBox="0 0 1200 363" aria-hidden="true">
  <defs><linearGradient id="arc2" x1="0" x2="1"><stop offset="0" stop-color="#1fa58f"/><stop offset="1" stop-color="#1b4fa8"/></linearGradient></defs>
  <path d="M0 190Q600 -60 1200 190V363H0Z" fill="#081734"/>
  <path d="M0 190Q600 -60 1200 190" fill="none" stroke="url(#arc2)" stroke-width="6"/>
</svg>
<div class="abs brand" style="left:0;width:1200px;text-align:center;top:4672px">Quillharbor</div>
<nav class="abs footer-nav" style="top:4754px">
  <span>Home</span><span>Solutions</span><span>How it works</span><span>Our market</span><span>Data value</span><span>IDE</span><span>About</span><span>Contact</span>
</nav>
<div class="abs contact-row" style="left:448px;top:4787px">
  <span><span class="ic">&#9742;</span>123-456-7890</span><span style="color:#6d7c95">|</span>
  <span><span class="ic">&#9993;</span>info@quillharbor.example</span>
</div>
<div class="abs social" style="top:4826px"><i></i><i></i><i></i><i></i><i></i></div>
<div class="abs" style="left:0;width:1200px;top:4900px;text-align:center;font-size:11px;color:#9fb0c8">© 2022 QUILLHARBOR &nbsp; / &nbsp; All Rights Reserved</div>

</body>
</html>
```